Consulting company business cards

We have a base design, but would be willing to update. We have a new logo/"tag" that needs to be added. Current business card design is attached for reference into our "style."

Industry/Entity Type

Business

Contact Information for Business Card

Should contain name and title, office number, mobile number if appropriate, e-mail, website, physical address, and company logo.

Font styles to use
Other font styles liked:
• See current card design on GorvandBCard

Colors
0455a3
85acd3
aaaaaa

Requirements
Must have
• Our colors are navy blue, gray, and a lighter blue
Nice to have
• Design that I can easily drop in new names/titles as we hire employees.

```html
<!DOCTYPE html>
<html lang="en">
<head>
<meta charset="utf-8">
<title>Corvell Business Cards</title>
<link href="https://fonts.googleapis.com/css2?family=Montserrat:wght@700&family=Questrial&display=swap" rel="stylesheet">
<style>
  :root {
    --navy: #083e6c;
    --navy-deep: #052c52;
    --sky: #6cc3e0;
    --grey: #8a8a8a;
    --paper: #ffffff;
    --paper-shade: #eceeef;
    --backdrop: #d9dcdf;
  }
  * { margin: 0; padding: 0; box-sizing: border-box; }
  html, body { width: 1200px; height: 900px; overflow: hidden; }
  body {
    background: var(--backdrop);
    font-family: "Questrial", "Century Gothic", sans-serif;
    position: relative;
  }
  .card {
    position: absolute;
    width: 560px;
    height: 320px;
    overflow: hidden;
    box-shadow: 0 14px 30px rgba(0,0,0,0.25);
  }

  /* Back of card */
  .card--back {
    left: 60px; top: 70px;
    background: linear-gradient(160deg, #0b4a80 0%, var(--navy) 50%, var(--navy-deep) 100%);
  }
  .card--back .stripe {
    position: absolute; left: 0; right: 0; top: 232px; height: 26px;
    background: var(--sky);
  }
  .card--back .foot {
    position: absolute; left: 0; right: 0; bottom: 0; height: 20px;
    background: var(--sky);
  }
  .card--back .brand { left: 100px; top: 96px; }
  .card--back .brand-name { color: #e9eef2; }
  .card--back .brand-mark { background: var(--sky); }
  .card--back .brand-tag { color: #a9c6dc; }

  /* Brand lockup */
  .brand { position: absolute; }
  .brand-row { display: flex; align-items: center; gap: 12px; }
  .brand-name {
    font-family: "Montserrat", sans-serif;
    font-weight: 700;
    font-size: 54px;
    letter-spacing: 1px;
    line-height: 1;
  }
  .brand-mark { width: 40px; height: 40px; border-radius: 50%; }
  .brand-tag {
    font-size: 13px;
    letter-spacing: 1.6px;
    margin-top: 6px;
    padding-left: 4px;
  }

  /* Front of card */
  .card--front {
    left: 580px; top: 500px;
    background: linear-gradient(180deg, var(--paper) 0%, var(--paper-shade) 100%);
  }
  .card--front .brand { right: 30px; top: 28px; }
  .card--front .brand-name { color: var(--navy); font-size: 46px; }
  .card--front .brand-mark { background: var(--sky); width: 34px; height: 34px; }
  .card--front .brand-tag { color: var(--grey); font-size: 11px; }

  .panel {
    position: absolute; left: 0; right: 0; top: 150px; bottom: 0;
    background: linear-gradient(170deg, #0a4677 0%, var(--navy-deep) 100%);
  }
  .panel-notch {
    position: absolute; left: 160px; top: -9px;
    width: 0; height: 0;
    border-left: 10px solid transparent;
    border-right: 10px solid transparent;
    border-bottom: 10px solid #0a4677;
  }
  .panel-band {
    position: absolute; left: 0; right: 0; bottom: 0; height: 28px;
    background: var(--sky);
  }

  .holder { position: absolute; left: 34px; top: 84px; }
  .holder-name {
    font-family: "Montserrat", sans-serif;
    font-weight: 700;
    font-size: 22px;
    color: var(--navy);
    letter-spacing: 0.5px;
  }
  .holder-title { font-size: 17px; color: var(--grey); margin-top: 2px; }

  .contacts {
    position: absolute; left: 34px; top: 168px;
    list-style: none; color: #e8f1f7; font-size: 15px;
  }
  .contacts li { display: flex; align-items: center; gap: 10px; height: 23px; }
  .contacts svg { width: 15px; height: 15px; flex: none; }

  .address {
    position: absolute; right: 30px; top: 168px;
    color: #e8f1f7; font-size: 14px; line-height: 1.45; text-align: right;
  }
</style>
</head>
<body>

  <section class="card card--back" aria-label="Card back">
    <div class="brand">
      <div class="brand-row">
        <span class="brand-name">CORVELL</span>
        <span class="brand-mark"></span>
      </div>
      <div class="brand-tag">A CLOUD CONSULTING COMPANY</div>
    </div>
    <div class="stripe"></div>
    <div class="foot"></div>
  </section>

  <section class="card card--front" aria-label="Card front">
    <div class="brand">
      <div class="brand-row">
        <span class="brand-name">CORVELL</span>
        <span class="brand-mark"></span>
      </div>
      <div class="brand-tag">A CLOUD CONSULTING COMPANY</div>
    </div>

    <div class="holder">
      <div class="holder-name">DANA GORVAND</div>
      <div class="holder-title">Office Manager</div>
    </div>

    <div class="panel">
      <span class="panel-notch"></span>
      <div class="panel-band"></div>
    </div>

    <ul class="contacts">
      <li>
        <svg viewBox="0 0 16 16"><rect width="16" height="16" rx="3" fill="#6cc3e0"/><path d="M5 3.5l2 2-1 1.2c.6 1.3 1.6 2.3 2.9 2.9L10 8.5l2 2-1.3 1.6C7.2 11.6 4.4 8.8 3.9 5.3z" fill="#083e6c"/></svg>
        555.014.2910
      </li>
      <li>
        <svg viewBox="0 0 16 16"><rect width="16" height="16" rx="3" fill="#6cc3e0"/><rect x="4.5" y="3" width="7" height="4" fill="#083e6c"/><rect x="3" y="7" width="10" height="4" rx="1" fill="#083e6c"/><rect x="5" y="10" width="6" height="3" fill="#083e6c"/></svg>
        555.014.2971
      </li>
      <li>
        <svg viewBox="0 0 16 16"><rect width="16" height="16" rx="3" fill="#6cc3e0"/><rect x="3" y="4.5" width="10" height="7" fill="none" stroke="#083e6c" stroke-width="1.3"/><path d="M3 4.5l5 4 5-4" fill="none" stroke="#083e6c" stroke-width="1.3"/></svg>
        dgorvand@corvelltech.com
      </li>
      <li>
        <svg viewBox="0 0 16 16"><rect width="16" height="16" rx="3" fill="#6cc3e0"/><circle cx="8" cy="8" r="4.8" fill="none" stroke="#083e6c" stroke-width="1.2"/><ellipse cx="8" cy="8" rx="2" ry="4.8" fill="none" stroke="#083e6c" stroke-width="1"/><path d="M3.2 8h9.6" stroke="#083e6c" stroke-width="1"/></svg>
        www.corvelltech.com
      </li>
    </ul>

    <address class="address">
      1850 W 48th St<br>
      Brookfield,<br>
      Indiana 46000
    </address>
  </section>

</body>
</html>
```